Business card design for online Mandarin Learning School

We need a business card design for our online language learning school called "Maple Bridge Online for Mandarin Learning". Our existing website is https://www.maplebridgeonline.com
We have our logo already. We would like to see our business card design that can make our online teaching services to be innovative, young, energetic and fun to learn. Prefer to have a certain level of color matching with our website. Apart from "Maple Bridge Online", need to specifically state "for Mandarin Learning" as well on the business card.

```html
<!DOCTYPE html>
<html lang="en">
<head>
<meta charset="utf-8">
<title>Maple Bridge Online – Business Card</title>
<link href="https://fonts.googleapis.com/css2?family=Roboto:wght@400;500;700&display=swap" rel="stylesheet">
<style>
  :root {
    --stage: #e2e3e4;
    --card-dark: #333a3c;
    --card-light: #f1f1f1;
    --teal: #1ea3b0;
    --coral: #d9585a;
    --grey: #7b7d7e;
    --grey-light: #a7a9aa;
    --text-dark: #4a4d50;
  }
  * { box-sizing: border-box; margin: 0; padding: 0; }
  html, body { width: 1200px; height: 1021px; overflow: hidden; }
  body {
    background: var(--stage);
    font-family: "Roboto", Arial, sans-serif;
    position: relative;
  }
  .card {
    position: absolute;
    left: 220px;
    width: 760px;
    height: 434px;
    overflow: hidden;
    box-shadow: 0 6px 18px rgba(0,0,0,.18);
  }
  .card--back { top: 46px; background: var(--card-dark); }
  .card--front { top: 541px; background: var(--card-light); }

  .stripe-band {
    position: absolute; left: 0; right: 0; bottom: 0; height: 22px;
    display: flex;
  }
  .stripe-band span { flex: 1; }
  .stripe-band .g { background: var(--grey); flex: 0.9; }
  .stripe-band .r { background: var(--coral); }
  .stripe-band .t { background: var(--teal); }

  .brand-name {
    color: var(--teal);
    font-weight: 500;
    letter-spacing: .04em;
    text-transform: uppercase;
    line-height: 1.25;
  }
  .card--back .brand {
    position: absolute; top: 150px; left: 0; right: 0;
    text-align: center;
  }
  .card--back .brand-name { font-size: 38px; }
  .card--back .brand-name small { display: block; font-size: 22px; letter-spacing: .12em; }
  .brand-mark {
    display: inline-block; width: 14px; height: 14px; border-radius: 50%;
    background: var(--coral); margin-bottom: 14px;
  }
  .card--back .site {
    position: absolute; top: 318px; left: 0; right: 0; text-align: center;
    font-size: 17px; letter-spacing: .14em; color: var(--grey-light);
  }
  .card--back .site b { color: var(--teal); font-weight: 500; }

  .card--front .brand { position: absolute; top: 60px; left: 46px; }
  .card--front .brand-name { font-size: 28px; }
  .card--front .brand-name small { display: block; font-size: 16px; letter-spacing: .1em; }

  .contact { position: absolute; left: 46px; top: 258px; list-style: none; }
  .contact li {
    display: flex; align-items: center; gap: 8px;
    font-size: 19px; color: var(--text-dark); line-height: 26px;
  }
  .contact svg { width: 16px; height: 16px; flex: none; }

  .person { position: absolute; right: 74px; top: 176px; text-align: right; }
  .person-name { font-size: 30px; font-weight: 700; color: var(--teal); }
  .person-role { font-size: 19px; color: var(--text-dark); margin-top: 2px; }
</style>
</head>
<body>

<section class="card card--back" aria-label="Card back">
  <div class="brand">
    <span class="brand-mark"></span>
    <p class="brand-name">Maple Bridge Online<small>for Mandarin Learning</small></p>
  </div>
  <p class="site">www.<b>maplebridgeonline</b>.com</p>
  <div class="stripe-band"><span class="g"></span><span class="r"></span><span class="t"></span><span class="g"></span><span class="r"></span><span class="t"></span><span class="g"></span></div>
</section>

<section class="card card--front" aria-label="Card front">
  <div class="brand">
    <p class="brand-name">Maple Bridge Online<small>for Mandarin Learning</small></p>
  </div>

  <ul class="contact">
    <li>
      <svg viewBox="0 0 16 16" aria-hidden="true"><path fill="#d9585a" d="M3.5 1h3l1 3.5-2 1.3a9 9 0 0 0 4.7 4.7l1.3-2 3.5 1v3c0 1-1 1.5-2 1.5C6.5 14 2 9.5 2 3c0-1 .5-2 1.5-2z"/></svg>
      (555) 218-4630
    </li>
    <li>
      <svg viewBox="0 0 16 16" aria-hidden="true"><rect x="1.5" y="3.5" width="13" height="9" fill="none" stroke="#d9585a" stroke-width="1.5"/><path d="M1.5 3.5 8 9l6.5-5.5" fill="none" stroke="#d9585a" stroke-width="1.5"/></svg>
      support@maplebridgeonline.com
    </li>
    <li>
      <svg viewBox="0 0 16 16" aria-hidden="true"><g fill="none" stroke="#d9585a" stroke-width="1.3"><circle cx="8" cy="8" r="6.5"/><ellipse cx="8" cy="8" rx="3" ry="6.5"/><path d="M1.5 8h13M2.5 5h11M2.5 11h11"/></g></svg>
      www.maplebridgeonline.com
    </li>
  </ul>

  <div class="person">
    <p class="person-name">Daniel Carter</p>
    <p class="person-role">Founder</p>
  </div>

  <div class="stripe-band"><span class="g"></span><span class="r"></span><span class="t"></span><span class="g"></span><span class="r"></span><span class="t"></span><span class="g"></span></div>
</section>

</body>
</html>
```